Billboard design for a dental office
Maple Ridge Dental
Creative Brief
Health
I will prefer it to be on a white background however, i am open to options, you may also include a nice smiling face to it. I need my logo to be incorporated on it and my phone number (407) 555-0187 in a very large text which should be visible from a long distance. i need a cutting edge design. The billboard dimensions should be 14'X48' The billboard should also say "Now we have the same day crown"

```html
<!DOCTYPE html>
<html lang="en">
<head>
<meta charset="utf-8">
<title>Maple Ridge Dental Billboard</title>
<link rel="stylesheet" href="https://fonts.googleapis.com/css2?family=Oswald:wght@500;600&family=Open+Sans:wght@600;700;800&family=Playfair+Display:ital,wght@1,700&display=swap">
<style>
  :root {
    --stage: #2b2b2b;
    --board-white: #ffffff;
    --warm-cream: #fde7c6;
    --orange: #f08a12;
    --orange-deep: #e06a05;
    --red: #d7261e;
    --ink: #3a3a3a;
    --badge-green: #2f5d33;
    --badge-text: #ffffff;
    --price-dark: #2a2a2a;
    --photo-light: #e8b896;
    --photo-mid: #b77a57;
    --photo-dark: #2a1812;
  }
  html, body {
    margin: 0;
    width: 1200px;
    height: 901px;
    overflow: hidden;
    background: var(--stage);
  }
  .billboard {
    position: absolute;
    left: 40px;
    top: 287px;
    width: 1120px;
    height: 327px;
    overflow: hidden;
    background: linear-gradient(115deg, var(--board-white) 0%, var(--board-white) 22%, var(--warm-cream) 40%, var(--orange) 62%);
    font-family: "Open Sans", sans-serif;
  }
  .hero-photo {
    position: absolute;
    right: 0;
    top: 0;
    width: 600px;
    height: 100%;
    clip-path: polygon(70px 0, 100% 0, 100% 100%, 0 100%);
    background: linear-gradient(100deg, var(--photo-dark) 0%, var(--photo-mid) 22%, var(--photo-light) 48%, var(--photo-mid) 78%, var(--photo-dark) 100%);
  }
  .tagline {
    position: absolute;
    left: 28px;
    top: 26px;
    margin: 0;
    color: var(--ink);
    font-size: 17px;
    font-weight: 700;
    font-style: italic;
    transform: rotate(-6deg);
    transform-origin: left bottom;
    white-space: nowrap;
  }
  .tagline .accent {
    font-family: "Playfair Display", serif;
    color: var(--red);
    font-size: 34px;
  }
  .brand {
    position: absolute;
    left: 36px;
    top: 116px;
    display: flex;
    align-items: center;
    gap: 16px;
  }
  .brand-mark {
    width: 64px;
    height: 64px;
    border-radius: 50%;
    background: var(--red);
  }
  .brand-name {
    margin: 0;
    font-family: "Oswald", sans-serif;
    font-weight: 600;
    font-size: 44px;
    line-height: 1;
    color: var(--ink);
    text-transform: uppercase;
  }
  .phone {
    position: absolute;
    left: 30px;
    top: 208px;
    display: flex;
    align-items: center;
    gap: 12px;
    color: var(--red);
    font-weight: 800;
    font-size: 48px;
    line-height: 1;
    letter-spacing: -0.5px;
  }
  .phone svg { width: 36px; height: 36px; fill: var(--red); }
  .offer-band {
    position: absolute;
    left: 0;
    bottom: 0;
    width: 520px;
    height: 42px;
    background: linear-gradient(90deg, var(--orange-deep), var(--orange));
    color: var(--board-white);
    font-weight: 700;
    font-style: italic;
    font-size: 21px;
    line-height: 42px;
    padding-left: 26px;
    box-sizing: border-box;
  }
  .special {
    position: absolute;
    left: 560px;
    top: 210px;
    display: flex;
    align-items: center;
  }
  .special-label {
    background: var(--badge-green);
    color: var(--badge-text);
    font-weight: 700;
    font-size: 19px;
    line-height: 1.15;
    padding: 10px 52px 10px 14px;
    border-radius: 6px;
    border: 2px solid var(--badge-text);
  }
  .special-price {
    width: 96px;
    height: 96px;
    margin-left: -44px;
    border-radius: 50%;
    background: var(--price-dark);
    border: 3px solid var(--badge-text);
    color: var(--badge-text);
    font-family: "Oswald", sans-serif;
    font-weight: 500;
    font-size: 44px;
    display: flex;
    align-items: center;
    justify-content: center;
  }
</style>
</head>
<body>
  <main class="billboard">
    <div class="hero-photo" role="img" aria-label="Photo of a smiling woman with dark hair showing white teeth"></div>

    <p class="tagline">Creating Beautiful <span class="accent">Smiles,</span> Excellence in Dentistry</p>

    <div class="brand">
      <div class="brand-mark"></div>
      <h1 class="brand-name">Maple Ridge Dental</h1>
    </div>

    <div class="phone">
      <svg viewBox="0 0 24 24" aria-hidden="true"><path d="M6.6 10.8a15.1 15.1 0 0 0 6.6 6.6l2.2-2.2a1 1 0 0 1 1-.25 11.4 11.4 0 0 0 3.6.57 1 1 0 0 1 1 1V20a1 1 0 0 1-1 1A17 17 0 0 1 3 4a1 1 0 0 1 1-1h3.5a1 1 0 0 1 1 1c0 1.25.2 2.45.57 3.57a1 1 0 0 1-.25 1z"/></svg>
      <span>(407) 555-0187</span>
    </div>

    <div class="offer-band">Now we have the same day crown</div>

    <div class="special">
      <div class="special-label">Exam, X-ray<br>and Cleaning</div>
      <div class="special-price">$77</div>
    </div>
  </main>
</body>
</html>
```